CV brochure for Top Management Position

I need me to introduce myself a brochure design for a CV brochure in. So sort of a resume in booklet format. The design should be serious for a convey on the other, the viewer that I stand for the new world of digitization. The brochure is intended to convey that I am a "Digital Leader". With the brochure boards, boards of directors and decision makers of enterprises should pay attention to my person. It must not be a 0815 design of the rod. The design should already be addressed with the front page of the topic Digital Leader, since the front page usually is the decisive criterion whether to continue dealing with the person or not. I am now CIO (IT manager) and wants to move with the brochure myself from this technique corner out and thus make it interesting for other positions. The positions are in absolute top management, the board, management, supervisory anchored and deal primarily with the digital transformation and the new digital world. So should appear with security on the front page a concise picture of me. but I am also very open to any alternative proposal brochure. Here you can see my current CV with picture and the basic content. The brochure is even more responsive to the social skills and not only to the technical projects implemented as before.

Target Market(s)

Top management, CxO level, supervisory boards, large companies, large Mittlestandsunternehmen

Industry/Entity Type

Management

Font styles to use
Serif
Sans Serif

Requirements
Must have
• see description
Nice to have
• see description
Should not have
• see description

```html
<!DOCTYPE html>
<html lang="de">
<head>
<meta charset="utf-8">
<title>Dr. Jonas Albrecht – Lebenslauf</title>
<link rel="stylesheet" href="https://fonts.googleapis.com/css2?family=Open+Sans:wght@400;600;700;800&family=Lato:wght@300;400;700&display=swap">
<style>
  :root {
    --navy: #2b3648;
    --navy-dark: #232d3d;
    --paper: #ffffff;
    --backdrop: #e8e9eb;
    --muted: #b7bcc5;
    --label: #aeb4be;
    --body-grey: #5d6470;
    --company-grey: #747a84;
    --marker: #a9adb4;
    --date-text: #c9ced6;
  }
  * { box-sizing: border-box; margin: 0; padding: 0; }
  html, body { width: 867px; height: 1200px; overflow: hidden; }
  body { background: var(--backdrop); font-family: "Open Sans", Arial, sans-serif; }

  .cv-page {
    position: absolute; left: 20px; top: 24px; width: 827px; height: 1152px;
    background: var(--paper); box-shadow: 0 2px 8px rgba(0,0,0,.12);
  }

  /* Sidebar */
  .sidebar {
    position: absolute; left: 0; top: 0; width: 363px; height: 100%;
    background: var(--navy); color: #fff;
  }
  .portrait {
    position: absolute; left: 111px; top: 49px; width: 142px; height: 142px;
    border-radius: 50%; border: 3px solid #fff;
    background: radial-gradient(circle at 50% 40%, #e7c3ae 0 28%, #c9ccd2 29% 60%, #3a3f48 61%);
  }
  .tagline {
    position: absolute; left: 0; width: 363px; top: 214px; text-align: center;
    font-size: 16.5px; font-weight: 600; color: var(--muted);
  }
  .facts {
    position: absolute; left: 30px; top: 260px; border-collapse: collapse;
    font-size: 13.8px;
  }
  .facts td { height: 23.8px; vertical-align: middle; }
  .facts .fact-label { width: 120px; color: var(--label); font-weight: 400; }
  .facts .fact-value { font-weight: 700; color: #fff; }

  .glance-title {
    position: absolute; left: 30px; top: 500px; font-size: 21px; font-weight: 700;
    color: var(--muted); padding-left: 10px; border-left: 5px solid var(--muted);
    line-height: 26px;
  }
  .glance {
    position: absolute; left: 30px; top: 544px; width: 320px;
    font-size: 13.4px; line-height: 17.5px; color: #fff;
  }
  .glance p { margin-bottom: 17px; }
  .glance strong { font-weight: 800; font-size: 15.6px; letter-spacing: .1px; }

  /* Main column */
  .main { position: absolute; left: 363px; top: 0; right: 0; height: 100%; }
  .name {
    position: absolute; left: 0; right: 0; top: 90px; text-align: center;
    font-size: 33px; font-weight: 700; color: var(--navy); letter-spacing: .3px;
  }
  .title-line {
    position: absolute; left: 0; right: 0; top: 141px; text-align: center;
    font-size: 13.3px; color: #7d838c;
  }
  .header-rule {
    position: absolute; left: 0; top: 179px; width: 462px; height: 3px; background: var(--navy);
  }
  .header-rule-end {
    position: absolute; left: 457px; top: 179px; width: 7px; height: 14px; background: var(--navy);
  }

  .section-title {
    position: absolute; left: 27px; top: 222px; font-size: 22.5px; font-weight: 600;
    color: var(--navy);
  }
  .job-meta {
    position: absolute; left: 27px; top: 240px; width: 440px;
    font-size: 13.2px; font-weight: 700; color: var(--company-grey); line-height: 16.8px;
  }
  .job-date {
    display: inline-block; width: 112px; margin-left: 16px; margin-right: 16px;
    background: var(--navy); color: var(--date-text); text-align: center;
    font-weight: 700; height: 16px; line-height: 16px; vertical-align: 0;
  }
  .job-role {
    position: absolute; left: 14px; top: 341px; height: 26px; padding-left: 11px;
    border-left: 5px solid var(--navy); line-height: 26px;
    font-size: 13.8px; font-weight: 700; color: var(--navy);
  }
  .achievements {
    position: absolute; left: 28px; top: 375px; list-style: none;
    font-family: "Lato", "Gill Sans", sans-serif; font-weight: 400;
    font-size: 12.6px; line-height: 16.3px; color: var(--body-grey);
  }
  .achievements li {
    position: relative; padding-left: 13px; margin-bottom: 4.4px; white-space: nowrap;
  }
  .achievements li::before {
    content: ""; position: absolute; left: 0; top: 5px; width: 7px; height: 7px;
    background: var(--marker);
  }
  .achievements b {
    font-family: "Open Sans", Arial, sans-serif; font-weight: 700; color: var(--navy); font-size: 13px;
  }
</style>
</head>
<body>
<article class="cv-page">
  <aside class="sidebar">
    <div class="portrait" role="img" aria-label="Porträtfoto von Dr. Jonas Albrecht"></div>
    <p class="tagline">Chief Digital Officer - Digital Leader</p>
    <table class="facts">
      <tr><td class="fact-label">Adresse</td><td class="fact-value">Lindenweg 12, 10115 Berlin</td></tr>
      <tr><td class="fact-label">Geburtsdaten</td><td class="fact-value">29. März 1978 in Konstanz</td></tr>
      <tr><td class="fact-label">Familienstand</td><td class="fact-value">verheiratet | 2 Kinder</td></tr>
      <tr><td class="fact-label">Mobil</td><td class="fact-value">+ 49 (0) 170 55 0192 44</td></tr>
      <tr><td class="fact-label">E-Mail</td><td class="fact-value">kontakt@albrecht.de</td></tr>
      <tr><td class="fact-label">Profil</td><td class="fact-value">www.netzprofil.de/albrecht</td></tr>
    </table>

    <h2 class="glance-title">Auf einen Blick</h2>
    <div class="glance">
      <p><strong>Kommunikationsstarke Führungspersönlichkeit</strong> mit mehrjähriger Erfahrung in Leitungsfunktionen im IT-Bereich, aktuell Chief Information Officer (CIO) und Chief Digital Officer (CDO)</p>
      <p>Umfangreiche <strong>Fachexpertise</strong> in: Konzeption und <strong>Weiterentwicklung von IT-Unternehmensstrategien</strong> | Effizienzsteigerung im IT-Bereich | <strong>Optimierung der IT-Service-Strukturen</strong> | Planung und Durchführung <strong>konzernweiter IT-Programme</strong></p>
      <p>Experte auf dem Gebiet der <strong>Transformation von Unternehmen in die digitale Welt</strong> (Industrie 4.0) | <strong>Etablierung der IT als Business Enabler</strong></p>
      <p>Führung von <strong>75 MA + ca. 20 (weltweite und externe)</strong>, davon 4 Führungskräfte | Budget i.H.v. <strong>22 Mio. €</strong> p.a.</p>
      <p><strong>Wissensmanager mit interkultureller Kompetenz</strong>, breitem Technologieverständnis sowie ausgeprägter Durchsetzungs- und Teamfähigkeit</p>
      <p><strong>Umsetzungsstark</strong> | lösungsorientiert | <strong>unternehmerisch</strong> | visionär</p>
    </div>
  </aside>

  <main class="main">
    <h1 class="name">Dr. Jonas Albrecht</h1>
    <p class="title-line">Chief Information Officer (CIO) | Ph.D. Wirtschaftsinformatik</p>
    <div class="header-rule"></div>
    <div class="header-rule-end"></div>

    <h2 class="section-title">Berufliche Erfahrungen</h2>
    <p class="job-meta" style="top:264px"><span class="job-date">10/2012</span>Heute&nbsp; Kessler Gruppe | Talheim |<br>www.kessler-gruppe.de Weltweiter Hersteller von zerspanenden Präzisionswerkzeugen | 7.000 MA weltweit in ca. 50 Ländern | 900 Mio. € Umsatz</p>

    <h3 class="job-role">Chief Information Officer/ Chief Digital Officer</h3>
    <ul class="achievements">
      <li><b>Verantwortung</b> der operativen sowie strategischen IT weltweit</li>
      <li><b>Verantwortung</b> der digitalen Transformation der Firma weltweit,<br>Umsetzung der Vision Kessler 2020</li>
      <li><b>Aufbau</b> einer IT-Strategie in Abstimmung mit Geschäftsführung und<br>Eigentümer</li>
      <li><b>Entwicklung</b> und Umsetzung einer ERP-Roadmap 2020, inkl.<br>Einführung CoreBase Hana, Einführung CoreBase One in ca. 40<br>Tochtergesellschaften weltweit</li>
      <li><b>Aufbau</b> eines IT-Risikomanagementsystems in Zusammenhang<br>mit IT-GRC-Strukturen</li>
      <li><b>Definition</b> einer zentralen e-Business Multichannel Architektur</li>
      <li><b>Aufbau</b> einer IT-Leistungsrechnung sowie eines IT-Controllings</li>
      <li><b>Aufbau</b> zweier IT Hubs in Asien und Amerika</li>
      <li><b>Neuausrichtung</b> der gesamten IT-Infrastruktur (Migration von<br>Nexor zu Calder Systems)</li>
      <li><b>Etablierung</b> einer IT-Projektmethodik</li>
      <li><b>Erarbeitung</b> eines ECM-Konzepts „Just-in-time Informationslogistik“</li>
      <li><b>Definition/Rollout</b> einer Prozessmodellierungssystematik unter<br>BPMN 2.0 und Flowtrace</li>
      <li><b>Aufteilung</b> der IT in Projektgeschäft und Katalog bzw. Standardg-<br>eschäft (vom Einkauf über Anforderungen bis hin zum Betrieb)</li>
      <li><b>Definition</b> einer neuen IT-Organisation nach dem Plan-Build-Run<br>Prinzip von ServiceNorm</li>
      <li><b>Entwicklung</b> einer Roadmap Industrie 4.0, Erprobung diverser<br>Industrie-4.0-Themen mit der Produktion, Erarbeitung einer<br>IT-Security-Strategie für alle Produktionswerke, Testen von neuen<br>„Wearables“ zum Einsatz in der Produktion, Vollautomatisierung<br>von Produktionswerken durch IT,</li>
      <li><b>Aufbau</b> einer neuen digitalen Einheit zur Erarbeitung von neuen<br>Geschäftsmodellen. Verantwortung: Führung von 75 MA + ca. 20<br>(weltweite und externe), davon 4 Führungskräfte | Budget i.H.v. 22<br>Mio. € Erfolge:</li>
      <li><b>Einführung</b> einer globalen ERP-Strategie, Einsparung von 1/3 der<br>Kosten bei jedem Rollout durch Einsatz der Mittelstandslösung<br>CoreBase-One, Verkürzung der Einführungszeiten von 1 Jahr auf 4<br>Monate sowie Erhöhung der Userzufriedenheit durch größere Usability<br>und Simplicity der ERP Anwendung</li>
      <li><b>Erstellung</b> und Umsetzung einer globalen IT-Strategie und komplette<br>Neustrukturierung der IT zu einer schnelleren und agileren Arbeitswei-<br>se (Etablierung einer Two Speed IT)</li>
      <li><b>Erstellung</b> einer digitalen Vision Kessler 2020</li>
      <li><b>Erzielung</b> erster Online-Umsätze mit dem neuen eBusiness Konzept</li>
    </ul>
  </main>
</article>
</body>
</html>
```